New Alcoholic Spiked Seltzer Line

We need a can design for a line of low calorie alcoholic seltzer. This product is a sparkling water and vodka drink with no sugar added in a slim 12 oz can.

This is a lighter, healthier, alternative to the sugary ready-to-drinks on the market. The product contains only 3 ingredients: Vodka, Water and Natural Flavors. It has only 100 calories but still has 5% alcohol, so you don't need to sacrifice alcohol to cut calories.

This product also does not contain any preservatives.

We want this design to communicate the following objectives to the consumer and in this order:

1. Appetizing product
2.Low calorie
3.Communicate the type of beverage (Spiked Seltzer)

The brand name of the product is VELKA.

The flavor of the product needed to be used for the design is Mango-Orange.

Comparable products are:

www.brisavelfizz.example/
https://www.tarnowbubble.example
https://quellrind.example/

The designs should not infringe or copy the creative directions of the products mentionned above. They are only given so that you can better understand the type of product we are developing.

Target Market(s)

Young Professional women between the ages of 25 and 44

Industry/Entity Type

Product

Colors

Designer to choose colors to be used in the design.

Requirements
Must have
• Design extendibility, meaning it can be adapted for other flavors.
• This is a new category in the market we are targeting, so consumers must easily be able to identify what type of product this is.

```html
<!DOCTYPE html>
<html lang="en">
<head>
<meta charset="utf-8">
<title>VELKA Spiked Seltzer – Mango-Orange Label</title>
<link rel="stylesheet" href="https://fonts.googleapis.com/css2?family=Questrial&family=Chelsea+Market&family=Oswald:wght@500&family=Open+Sans:wght@600&display=swap">
<style>
  :root {
    --backdrop: #ececec;
    --label-white: #fbfbfb;
    --orange-deep: #c92a12;
    --orange-mid: #e8461c;
    --mango-glow: #ff9a3c;
    --brand-ink: #2f3438;
    --type-grey: #5a5e62;
    --stripe-white: #ffffff;
  }
  html, body {
    margin: 0;
    padding: 0;
    width: 968px;
    height: 1200px;
    overflow: hidden;
    background: var(--backdrop);
  }
  .canvas {
    position: relative;
    width: 968px;
    height: 1200px;
  }
  .can-label {
    position: absolute;
    left: 274px;
    top: 100px;
    width: 420px;
    height: 1000px;
    box-shadow: 0 10px 30px rgba(0,0,0,0.12);
  }
  .category {
    font-family: "Questrial", sans-serif;
    font-size: 40px;
    fill: var(--type-grey);
  }
  .brand-name {
    font-family: "Questrial", sans-serif;
    font-size: 104px;
    fill: var(--brand-ink);
  }
  .flavour {
    font-family: "Chelsea Market", cursive;
    font-size: 40px;
    fill: var(--stripe-white);
  }
  .abv {
    font-family: "Oswald", sans-serif;
    font-weight: 500;
    font-size: 46px;
    fill: var(--stripe-white);
  }
  .claim {
    font-family: "Open Sans", sans-serif;
    font-weight: 600;
    font-size: 24px;
    letter-spacing: 1px;
    fill: var(--stripe-white);
  }
</style>
</head>
<body>
<main class="canvas">
  <svg class="can-label" viewBox="0 0 420 1000" width="420" height="1000" xmlns="http://www.w3.org/2000/svg">
    <defs>
      <linearGradient id="orangeBand" x1="0" y1="0" x2="1" y2="0">
        <stop offset="0" stop-color="var(--orange-deep)"/>
        <stop offset="0.5" stop-color="var(--orange-mid)"/>
        <stop offset="1" stop-color="var(--orange-deep)"/>
      </linearGradient>
      <radialGradient id="mangoGlow" cx="0.5" cy="0.55" r="0.5">
        <stop offset="0" stop-color="var(--mango-glow)" stop-opacity="0.85"/>
        <stop offset="1" stop-color="var(--mango-glow)" stop-opacity="0"/>
      </radialGradient>
    </defs>

    <rect class="label-base" x="0" y="0" width="420" height="1000" fill="var(--label-white)"/>
    <polygon class="flavour-band" points="0,560 420,260 420,1000 0,1000" fill="url(#orangeBand)"/>
    <ellipse class="mango-glow" cx="250" cy="620" rx="230" ry="260" fill="url(#mangoGlow)"/>
    <polygon class="stripe-wide" points="0,730 420,430 420,456 0,756" fill="var(--stripe-white)"/>
    <polygon class="stripe-thin" points="0,772 420,472 420,481 0,781" fill="var(--stripe-white)"/>

    <text class="category" x="210" y="100" text-anchor="middle">Spiked Seltzer</text>
    <text class="brand-name" x="210" y="230" text-anchor="middle" textLength="330" lengthAdjust="spacing">VELKA</text>

    <text class="flavour" x="210" y="840" text-anchor="middle">mango-orange</text>
    <line class="flavour-rule" x1="90" y1="862" x2="330" y2="862" stroke="var(--stripe-white)" stroke-width="2"/>
    <text class="abv" x="210" y="918" text-anchor="middle">5% ALC/VOL</text>
    <text class="claim" x="210" y="948" text-anchor="middle">LOW CALORIES</text>
  </svg>
</main>
</body>
</html>
```